Business Card Design

Company is a Commercial Building Company specialising in New Construction and existing refurbishments

Industry/Entity Type

Business

Contact Information for Business Card

Dale Mercer
Construction Manager
E Dale@harbridgebuilding.com.au
M 0400 213 947
Mail 27 Tarrant Rise Marlow Bay WA 6299

```html
<!DOCTYPE html>
<html lang="en">
<head>
<meta charset="utf-8">
<title>Harbridge Building &amp; Construction — Business Card</title>
<link href="https://fonts.googleapis.com/css2?family=Lato:wght@400;700;900&display=swap" rel="stylesheet">
<style>
  :root {
    --stage: #2b2b2b;
    --card: #ffffff;
    --card-shade: #f1f1f1;
    --teal: #1aa6c1;
    --orange: #e5892a;
    --ink: #3c4250;
    --ink-soft: #555b66;
  }
  * { box-sizing: border-box; margin: 0; padding: 0; }
  html, body {
    width: 1200px; height: 997px; overflow: hidden;
    background: var(--stage);
    font-family: "Lato", Arial, sans-serif;
  }
  .stage { position: relative; width: 1200px; height: 997px; }

  .card {
    position: absolute;
    width: 620px; height: 376px;
    background: linear-gradient(135deg, var(--card) 0%, var(--card-shade) 100%);
    overflow: hidden;
  }
  .card--back { left: 90px; top: 70px; }
  .card--front { left: 490px; top: 520px; }

  .card__bands {
    position: absolute; left: 0; bottom: 0;
    width: 620px; height: 40px;
  }

  .brand {
    display: flex; align-items: center; gap: 14px;
    color: var(--ink);
    font-weight: 700;
    line-height: 1.05;
    text-transform: uppercase;
  }
  .brand__mark { background: var(--teal); flex: none; }
  .brand__name { display: block; white-space: nowrap; }
  .brand__name span { display: block; }

  /* Back of card */
  .card--back .brand {
    position: absolute; left: 150px; top: 110px;
    font-size: 28px; letter-spacing: 0.5px;
  }
  .card--back .brand__mark { width: 46px; height: 46px; }
  .tagline {
    position: absolute; left: 0; right: 0; top: 240px;
    text-align: center;
    font-size: 15px; font-weight: 700;
    color: var(--ink-soft);
  }

  /* Front of card */
  .card--front .brand {
    position: absolute; right: 36px; top: 42px;
    font-size: 21px; letter-spacing: 0.4px;
  }
  .card--front .brand__mark { width: 34px; height: 34px; }

  .person { position: absolute; left: 44px; top: 150px; }
  .person__name { color: var(--orange); font-size: 21px; font-weight: 900; }
  .person__role { color: var(--ink); font-size: 16px; margin-top: 2px; }

  .contacts {
    position: absolute; left: 44px; top: 236px;
    list-style: none;
    color: var(--ink-soft); font-size: 15px;
  }
  .contacts li { display: flex; align-items: center; gap: 12px; height: 28px; white-space: nowrap; }
  .contacts svg { width: 16px; height: 16px; flex: none; }
</style>
</head>
<body>
<main class="stage">

  <section class="card card--back" aria-label="Business card, back">
    <div class="brand">
      <span class="brand__mark"></span>
      <span class="brand__name"><span>Harbridge Building</span><span>&amp; Construction</span></span>
    </div>
    <p class="tagline">New Construction and existing refurbishments</p>
    <svg class="card__bands" viewBox="0 0 620 40" aria-hidden="true">
      <polygon points="0,14 300,14 326,40 0,40" fill="var(--teal)"/>
      <polygon points="312,26 620,26 620,40 326,40" fill="var(--orange)"/>
    </svg>
  </section>

  <section class="card card--front" aria-label="Business card, front">
    <div class="brand">
      <span class="brand__mark"></span>
      <span class="brand__name"><span>Harbridge Building</span><span>&amp; Construction</span></span>
    </div>

    <div class="person">
      <p class="person__name">Dale Mercer</p>
      <p class="person__role">Construction Manager</p>
    </div>

    <ul class="contacts">
      <li>
        <svg viewBox="0 0 16 16" aria-hidden="true"><rect x="3.5" y="1" width="9" height="14" rx="1.5" fill="none" stroke="var(--teal)" stroke-width="1.6"/><line x1="7" y1="12.5" x2="9" y2="12.5" stroke="var(--teal)" stroke-width="1.4"/></svg>
        0400 213 947
      </li>
      <li>
        <svg viewBox="0 0 16 16" aria-hidden="true"><rect x="1" y="3" width="14" height="10" fill="var(--teal)"/><polyline points="1,3 8,9 15,3" fill="none" stroke="#fff" stroke-width="1.3"/></svg>
        Dale@harbridgebuilding.com.au
      </li>
      <li>
        <svg viewBox="0 0 16 16" aria-hidden="true"><path d="M8 1a5 5 0 0 0-5 5c0 4 5 9 5 9s5-5 5-9a5 5 0 0 0-5-5z" fill="var(--teal)"/><circle cx="8" cy="6" r="2" fill="#fff"/></svg>
        27 Tarrant Rise Marlow Bay WA 6299
      </li>
    </ul>

    <svg class="card__bands" viewBox="0 0 620 40" aria-hidden="true">
      <polygon points="0,14 300,14 326,40 0,40" fill="var(--teal)"/>
      <polygon points="312,14 620,14 620,24 322,24" fill="var(--orange)"/>
    </svg>
  </section>

</main>
</body>
</html>
```